依頼詳細
社屋新築工事に伴い、独立看板の設置が必要となりました。
ロゴを含む看板全体のデザインを希望します。
サイズにつきまして、配置図の情報をもとにご提案いただきたいです。

■看板についての要望
・杉浦製作所のイメージに相応しい看板
・本社屋に来客した人に分かる看板
・杉浦製作所のイメージを伝えるような看板
・配置に関して駐車場に車両を駐車してもわかる看板

■サイズ
看板の大きさは、タテ・ヨコは、5.0×0.9~1.2m又は0.9~1.2×5.0mでお願いします。
高さは最大6mくらいでお願いします。
ヨコ長の場合は車両より上に設置予定。
※配置図を提供いたします。こちら考慮の上、デザイン制作をお願いいたします。

■提供資料
・建物 パース(完成イメージ)
・配置図
・ロゴ画像(HPより利用ください)

その他不明点は、やり取りの中で相談しながら進めさせてください。
記載項目
会社名「株式会社 杉浦製作所」/電話番号「TEL:0493-61-2740」/ロゴ「Sk」のマークのもの 看板の表示項目で会社名以外はデザイナーさんのイメージで判断下さい。
希望イメージ
シンプル 複雑
単色 カラフル
暗い 明るい
日常 高級
遊び心 厳粛
未来的 伝統的
女性的 男性的
希望する色
納品ファイル
• 高解像度JPG (.jpg)
• PNG形式 (.png)
補足説明
■ 選んだ理由

施主様に選考頂きました。
シンプルで目立つもので選びましたと話をされていました。

■ 提案者全員のお礼・コメント

たくさんのすてきなデザインを作成頂きましてありがとうございました。
今回はじめてツクリバを利用しました。
色々とシステムが呑み込めず、上手く出来ませんでしたが、
また、今後もこのうような案件がありましたら利用しようと思います。
今回参加頂きましたツクリバーの皆様、ありがとうございました。

```html
<!DOCTYPE html>
<html lang="ja">
<head>
<meta charset="utf-8">
<title>杉浦製作所 独立看板</title>
<link href="https://fonts.googleapis.com/css2?family=Noto+Sans+JP:wght@400;500;700&display=swap" rel="stylesheet">
<style>
  :root {
    --coral: #e0584d;
    --coral-soft: #f3c9c3;
    --ink: #2b2b2b;
    --label-line: #8fc7c7;
    --paper: #ffffff;
    --page: #ffffff;
  }
  * { box-sizing: border-box; margin: 0; padding: 0; }
  html, body {
    width: 846px; height: 1200px; overflow: hidden;
    background: var(--page);
    font-family: "Noto Sans JP", sans-serif;
    color: var(--ink);
  }
  .signboard {
    position: absolute;
    left: 276px; top: 28px;
    width: 296px; height: 1136px;
    background: var(--coral);
    border-radius: 4px;
  }
  .tagline {
    position: absolute; top: 14px; left: 0; width: 100%;
    text-align: center; color: var(--paper);
    font-size: 17px; font-weight: 500; letter-spacing: 3px;
  }
  .brand-mark {
    position: absolute; top: 50px; left: 50%;
    transform: translateX(-50%);
    display: flex; align-items: center; gap: 8px;
    color: var(--paper);
  }
  .brand-mark .dot {
    width: 52px; height: 52px; border-radius: 50%;
    border: 3px solid var(--paper);
    display: flex; align-items: center; justify-content: center;
    font-size: 24px; font-weight: 500;
  }
  .panel {
    position: absolute; top: 150px; left: 14px;
    width: 268px; height: 816px;
    background: var(--paper);
  }
  .features {
    display: flex; justify-content: space-between;
    padding: 0 12px; margin-top: 24px;
  }
  .feature {
    width: 58px; height: 44px;
    border: 2px solid var(--label-line); border-radius: 4px;
    display: flex; align-items: center; justify-content: center;
    font-size: 15px; color: var(--ink);
  }
  .company-type {
    position: absolute; top: 204px; left: 50%;
    transform: translateX(-50%);
    writing-mode: vertical-rl;
    font-size: 26px; font-weight: 500; letter-spacing: 4px;
  }
  .company-name {
    position: absolute; top: 360px; left: 50%;
    transform: translateX(-50%);
    writing-mode: vertical-rl;
    font-size: 64px; font-weight: 400; letter-spacing: 10px;
    line-height: 1;
  }
  .photo-strip {
    position: absolute; top: 966px; left: 14px;
    width: 268px; height: 114px;
    display: flex; gap: 2px; background: var(--paper);
  }
  .photo-strip div { flex: 1; }
  .photo-towel { background: linear-gradient(160deg, #d9dde2, #f7f7f7 55%, #e8c9c4); }
  .photo-herb { background: linear-gradient(160deg, #cfe3c2, #6fa45a 60%, #3e7a35); }
  .photo-pouch { background: linear-gradient(160deg, #e6e6e6, #f3d3cc 55%, #d8b8b0); }
  .contact {
    position: absolute; top: 1084px; left: 0; width: 100%;
    display: flex; align-items: center; justify-content: center; gap: 10px;
    color: var(--paper); font-size: 24px; font-weight: 500; letter-spacing: 1px;
  }
  .contact .icon {
    width: 28px; height: 28px; border: 2px solid var(--paper); border-radius: 4px;
    display: flex; align-items: center; justify-content: center;
  }
</style>
</head>
<body>
  <div class="signboard">
    <p class="tagline">マグネシウムのチカラ</p>
    <div class="brand-mark"><span class="dot">Sk</span></div>

    <div class="panel">
      <div class="features">
        <span class="feature">洗浄</span>
        <span class="feature">除菌</span>
        <span class="feature">消臭</span>
      </div>
      <p class="company-type">株式会社</p>
      <h1 class="company-name">杉浦製作所</h1>
    </div>

    <div class="photo-strip">
      <div class="photo-towel" role="img" aria-label="白いタオルの写真"></div>
      <div class="photo-herb" role="img" aria-label="緑のハーブの写真"></div>
      <div class="photo-pouch" role="img" aria-label="布製の小袋の写真"></div>
    </div>

    <p class="contact">
      <span class="icon">
        <svg width="16" height="16" viewBox="0 0 24 24" aria-hidden="true"><path fill="#fff" d="M6.6 10.8a15 15 0 0 0 6.6 6.6l2.2-2.2a1 1 0 0 1 1-.25 11.4 11.4 0 0 0 3.6.57 1 1 0 0 1 1 1V20a1 1 0 0 1-1 1A17 17 0 0 1 3 4a1 1 0 0 1 1-1h3.5a1 1 0 0 1 1 1c0 1.25.2 2.45.57 3.57a1 1 0 0 1-.25 1z"/></svg>
      </span>
      0493-61-2740
    </p>
  </div>
</body>
</html>
```